Innovative Event Ticketing Start Up. Needs a Web Design

We need a web design for a new company based in London called 'Bandwick'. We are a platform which facilitates the building of groups of customers for events. As more people commit to an event, the price incrementally decreases. We would like there to be an emphasis on the sharing element and the decreasing price with higher participation.

Any quieres please email me at rlvo57@mailtrove.net

Target Market(s)

18-30 year olds who are active and savvy across social media sites

Industry/Entity Type

Events

Number of Pages Required

3 page

Font styles to use
Other font styles liked:
• Phi Roman

Requirements
Must have
• Each event offering runs for a limited time so a countdown timer is also to be included as well as a counter of number of participants (please find example attached).
• The interface needs to have the options for 'Live 'Music', 'Nightlife', 'Festivals', 'Comedy' and 'Everything Else'. Also
• A 'featured' section, for our promoted events
• Social sharing icons for Chatterbarn, Quillow, PingMesh, SMS and Email
• Room the inclusion of a video
• Pages for clients to sign up - registering details ect.
• Content is still being completed, so room available to add when ready
Nice to have
• An interface design we like as a guiding templates on is https://kumvoxapp.com/
• Zamo wordpress theme is also of interest.
• Scroll over clicking for main interface and also for the event once clicked upon.
• Event pages similar desgin to kumvox with same features such as Trelvo Charts but also participant counter and affiliate marketing options.
Should not have
• CMS no longer necessary

```html
<!DOCTYPE html>
<html lang="en">
<head>
<meta charset="utf-8">
<title>Bandwick – Events</title>
<link rel="stylesheet" href="https://fonts.googleapis.com/css2?family=Open+Sans:wght@400;600;700&display=swap">
<style>
:root{
  --orange:#e8561f;
  --orange-light:#f07a3c;
  --ink:#333;
  --muted:#777;
  --light:#efefef;
  --white:#fff;
  --dark:#1d1f22;
  --dark-2:#2b2d30;
  --footer:#262626;
  --footer-bar:#1a1a1a;
}
*{box-sizing:border-box;margin:0;padding:0}
html,body{width:1200px;height:3084px;overflow:hidden}
body{font-family:"Open Sans",Arial,sans-serif;color:var(--ink);background:var(--white);font-size:14px}
.wrap{width:1000px;margin:0 auto}
.section-title{text-align:center;font-size:30px;font-weight:400}

/* header */
.site-header{height:146px;background:var(--white);position:relative}
.top-links{position:absolute;right:100px;top:10px;font-size:13px;color:var(--muted);display:flex;gap:18px}
.top-links span::before{content:"";display:inline-block;width:8px;height:8px;border-radius:50%;background:var(--orange);margin-right:6px}
.brand{position:absolute;left:100px;top:48px;display:flex;align-items:center;gap:12px}
.brand-mark{width:46px;height:46px;background:var(--orange);border-radius:6px}
.brand-name{font-size:34px;font-weight:600;color:var(--orange)}
.main-nav{position:absolute;left:520px;top:56px;display:flex;gap:6px}
.main-nav a{display:block;padding:30px 26px 14px;font-size:14px;color:var(--ink);text-decoration:none}
.main-nav a.active{background:var(--orange);color:var(--white);margin-top:-56px;padding-top:86px}

/* hero */
.hero{height:452px;position:relative;background:radial-gradient(ellipse at 55% 25%,#f3c8a0 0%,#c98a66 22%,#5e3d3a 55%,#1a1416 100%)}
.hero-title{position:absolute;top:210px;width:100%;text-align:center;font-size:38px;font-weight:700;color:var(--orange)}
.hero-arrow{position:absolute;top:212px;width:14px;height:24px}
.hero-arrow.left{left:24px}.hero-arrow.right{right:24px}

/* welcome */
.welcome{height:258px;padding-top:34px;text-align:center}
.welcome p{width:880px;margin:20px auto 0;font-size:12px;line-height:19px;color:var(--muted)}
.btn{display:inline-block;background:var(--orange);color:var(--white);font-size:14px;padding:9px 24px}
.welcome .btn{margin-top:20px}

/* events */
.upcoming{height:409px;background:linear-gradient(180deg,#1b2530,#242a33);color:var(--white);padding-top:40px}
.cards{display:flex;gap:20px;margin-top:30px}
.card{width:235px}
.card-photo{height:170px}
.meta-row{display:flex;align-items:center;gap:10px;font-size:11px;margin-top:10px}
.share{border:1px solid currentColor;padding:1px 8px;border-radius:2px;margin-left:auto}
.meta-line{font-size:12px;margin-top:7px;display:flex;align-items:center;gap:6px}
.dot{width:7px;height:7px;border-radius:50%;background:var(--orange);display:inline-block}

.featured{height:431px;background:var(--light);padding-top:28px}
.featured .card-photo{height:165px}
.featured .meta-line{color:var(--muted)}
.card-cat{font-size:14px;margin-top:10px}
.card-sub{font-size:12px;color:var(--muted);margin-top:4px}

/* targets */
.band{height:328px;background:linear-gradient(180deg,#2c1a0e,#4a2a12 50%,#21140c);color:var(--white);padding-top:30px}
.targets{display:flex;justify-content:space-around;margin-top:36px;padding:0 60px}
.target{text-align:center;font-size:12px}
.target svg{display:block;margin:0 auto 10px}

/* video */
.videos{height:374px;background:var(--light);position:relative}
.video-frame{position:absolute;left:100px;top:60px;width:390px;height:250px;background:linear-gradient(135deg,#c9762e,#5a2a14 60%,#1a0d08)}
.play{position:absolute;left:165px;top:95px}
.video-copy{position:absolute;left:620px;top:64px;width:480px}
.video-copy h2{color:var(--orange);font-size:20px;font-weight:600}
.video-copy p{font-size:12px;line-height:19px;color:var(--muted);margin:14px 0 24px}

/* contact */
.contact{height:274px;background:linear-gradient(135deg,#3a3c3f,#2c2e31 50%,#3a3b3d);color:var(--white);position:relative}
.contact-info{position:absolute;left:160px;top:24px;font-size:14px;line-height:34px}
.contact-info h3,.reg h3{font-size:18px;font-weight:400;margin-bottom:10px}
.contact-info div{display:flex;align-items:center;gap:10px}
.reg{position:absolute;left:600px;top:24px;width:440px;text-align:center}
.reg-grid{display:grid;grid-template-columns:1fr 1fr;gap:12px 20px;margin-top:6px}
.field{height:32px;border:1px solid var(--orange);background:rgba(0,0,0,.25);font-size:12px;color:#ccc;text-align:left;padding:7px 10px;position:relative}
.field.select::after{content:"";position:absolute;right:10px;top:13px;border:5px solid transparent;border-top-color:#ccc}
.reg .submit{display:inline-block;margin-top:18px;border:1px solid #aaa;padding:5px 28px;font-size:13px}

/* footer */
.site-footer{height:400px;background:var(--footer);color:#ddd;position:relative}
.foot-col{position:absolute;top:32px}
.foot-col h4{font-size:15px;font-weight:600;margin-bottom:12px}
.links li{list-style:none;font-size:12px;line-height:20px;color:#aaa}
.news p{font-size:12px;color:#aaa;margin-bottom:12px}
.news .input{width:260px;height:28px;background:var(--white);color:#999;font-size:12px;padding:5px 10px}
.news .btn{margin-top:16px;font-size:12px;padding:6px 16px}
.social{display:flex;flex-direction:column;gap:6px;font-size:13px;color:var(--orange)}
.footer-bar{position:absolute;bottom:0;left:0;width:100%;height:28px;background:var(--footer-bar);font-size:11px;color:#888;text-align:center;line-height:28px}
</style>
</head>
<body>

<header class="site-header">
  <div class="top-links"><span>Register</span><span>Login</span></div>
  <div class="brand"><span class="brand-mark"></span><span class="brand-name">Bandwick</span></div>
  <nav class="main-nav">
    <a class="active">Home</a><a>About</a><a>Services</a><a>Events</a><a>Contacts</a>
  </nav>
</header>

<section class="hero" role="img" aria-label="Crowd with raised hands at a festival against bright stage lights">
  <svg class="hero-arrow left" viewBox="0 0 14 24"><path d="M12 2 2 12l10 10" fill="none" stroke="#fff" stroke-width="2"/></svg>
  <h1 class="hero-title">EXPLORE FUN AND FESTIVALS</h1>
  <svg class="hero-arrow right" viewBox="0 0 14 24"><path d="M2 2l10 10L2 22" fill="none" stroke="#fff" stroke-width="2"/></svg>
</section>

<section class="welcome">
  <h2 class="section-title">Welcome To Bandwick</h2>
  <p>Bandwick brings people together around the events they love. Join a group for a gig, a club night or a festival and watch the ticket price fall as more friends commit. Share every event with your crowd, follow the countdown, and grab your place before the offer closes. The more people join, the less everyone pays, so invite widely and enjoy the night together with the best seats at the best price.</p>
  <span class="btn">View More</span>
</section>

<section class="upcoming">
  <div class="wrap">
    <h2 class="section-title">Upcoming Events</h2>
    <div class="cards">
      <div class="card"><div class="card-photo" role="img" aria-label="Friends at a night out" style="background:linear-gradient(135deg,#6a4a3a,#2a1a14)"></div>
        <div class="meta-row"><span>♥ 67</span><span>◷ 22</span><span>✎ 5.7K</span><span class="share">Share</span></div>
        <div class="meta-line"><span class="dot"></span>Nov 5, 2016 @ 10:00 pm</div>
        <div class="meta-line"><span class="dot"></span>Club Name</div></div>
      <div class="card"><div class="card-photo" role="img" aria-label="Concert stage with pink lights" style="background:linear-gradient(135deg,#b8466a,#3a1a3a)"></div>
        <div class="meta-row"><span>♥ 67</span><span>◷ 22</span><span>✎ 5.7K</span><span class="share">Share</span></div>
        <div class="meta-line"><span class="dot"></span>Nov 5, 2016 @ 10:00 pm</div>
        <div class="meta-line"><span class="dot"></span>Club Name</div></div>
      <div class="card"><div class="card-photo" role="img" aria-label="Crowd under purple stage lights" style="background:linear-gradient(135deg,#5a5ab0,#1a1a3a)"></div>
        <div class="meta-row"><span>♥ 67</span><span>◷ 22</span><span>✎ 5.7K</span><span class="share">Share</span></div>
        <div class="meta-line"><span class="dot"></span>Nov 5, 2016 @ 10:00 pm</div>
        <div class="meta-line"><span class="dot"></span>Club Name</div></div>
      <div class="card"><div class="card-photo" role="img" aria-label="Festival crowd at a red lit stage" style="background:linear-gradient(135deg,#c0402a,#2a1010)"></div>
        <div class="meta-row"><span>♥ 67</span><span>◷ 22</span><span>✎ 5.7K</span><span class="share">Share</span></div>
        <div class="meta-line"><span class="dot"></span>Nov 5, 2016 @ 10:00 pm</div>
        <div class="meta-line"><span class="dot"></span>Club Name</div></div>
    </div>
  </div>
</section>

<section class="featured">
  <div class="wrap">
    <h2 class="section-title">Feature Events</h2>
    <div class="cards">
      <div class="card"><div class="card-photo" role="img" aria-label="Group of friends celebrating" style="background:linear-gradient(135deg,#6a8a4a,#2a3a20)"></div>
        <div class="meta-line"><span class="dot"></span>Nov 5, 2016 @ 10:00 pm</div>
        <div class="meta-line"><span class="dot"></span>Club Name</div>
        <div class="card-cat">EVENTS</div><div class="card-sub">Lorem ipsum</div>
        <div class="meta-row" style="color:var(--muted)"><span>♥ 67</span><span>◷ 22</span><span>✎ 5.7K</span><span class="share">Share</span></div></div>
      <div class="card"><div class="card-photo" role="img" aria-label="Friends laughing at a party" style="background:linear-gradient(135deg,#d8b894,#6a4a30)"></div>
        <div class="meta-line"><span class="dot"></span>Nov 5, 2016 @ 10:00 pm</div>
        <div class="meta-line"><span class="dot"></span>Club Name</div>
        <div class="card-cat">EVENTS</div><div class="card-sub">Lorem ipsum</div>
        <div class="meta-row" style="color:var(--muted)"><span>♥ 67</span><span>◷ 22</span><span>✎ 5.7K</span><span class="share">Share</span></div></div>
      <div class="card"><div class="card-photo" role="img" aria-label="Young people taking a group photo" style="background:linear-gradient(135deg,#e0c8b0,#8a6a50)"></div>
        <div class="meta-line"><span class="dot"></span>Nov 5, 2016 @ 10:00 pm</div>
        <div class="meta-line"><span class="dot"></span>Club Name</div>
        <div class="card-cat">EVENTS</div><div class="card-sub">Lorem ipsum</div>
        <div class="meta-row" style="color:var(--muted)"><span>♥ 67</span><span>◷ 22</span><span>✎ 5.7K</span><span class="share">Share</span></div></div>
      <div class="card"><div class="card-photo" role="img" aria-label="Friends smiling outdoors" style="background:linear-gradient(135deg,#c8a0a8,#6a4050)"></div>
        <div class="meta-line"><span class="dot"></span>Nov 5, 2016 @ 10:00 pm</div>
        <div class="meta-line"><span class="dot"></span>Club Name</div>
        <div class="card-cat">EVENTS</div><div class="card-sub">Lorem ipsum</div>
        <div class="meta-row" style="color:var(--muted)"><span>♥ 67</span><span>◷ 22</span><span>✎ 5.7K</span><span class="share">Share</span></div></div>
    </div>
  </div>
</section>

<section class="band">
  <h2 class="section-title">Band Together</h2>
  <div class="targets">
    <div class="target"><svg width="116" height="116" viewBox="0 0 116 116"><circle cx="58" cy="58" r="52" fill="none" stroke="#fff" stroke-width="5"/><path d="M58 6a52 52 0 0 1 49 35" fill="none" stroke="var(--orange)" stroke-width="5"/><text x="58" y="62" text-anchor="middle" fill="#fff" font-size="26" font-family="Open Sans,sans-serif">500</text><text x="58" y="82" text-anchor="middle" fill="#fff" font-size="11" font-family="Open Sans,sans-serif">Target</text></svg>Lorem ipsum</div>
    <div class="target"><svg width="116" height="116" viewBox="0 0 116 116"><circle cx="58" cy="58" r="52" fill="none" stroke="#fff" stroke-width="5"/><path d="M58 6a52 52 0 0 1 52 52" fill="none" stroke="var(--orange)" stroke-width="5"/><text x="58" y="62" text-anchor="middle" fill="#fff" font-size="26" font-family="Open Sans,sans-serif">680</text><text x="58" y="82" text-anchor="middle" fill="#fff" font-size="11" font-family="Open Sans,sans-serif">Target</text></svg>Lorem ipsum</div>
    <div class="target"><svg width="116" height="116" viewBox="0 0 116 116"><circle cx="58" cy="58" r="52" fill="none" stroke="#fff" stroke-width="5"/><path d="M58 6a52 52 0 0 1 45 78" fill="none" stroke="var(--orange)" stroke-width="5"/><text x="58" y="62" text-anchor="middle" fill="#fff" font-size="26" font-family="Open Sans,sans-serif">980</text><text x="58" y="82" text-anchor="middle" fill="#fff" font-size="11" font-family="Open Sans,sans-serif">Target</text></svg>Lorem ipsum</div>
    <div class="target"><svg width="116" height="116" viewBox="0 0 116 116"><circle cx="58" cy="58" r="52" fill="none" stroke="#fff" stroke-width="5"/><path d="M58 6a52 52 0 0 1 0 104" fill="none" stroke="var(--orange)" stroke-width="5"/><text x="58" y="62" text-anchor="middle" fill="#fff" font-size="26" font-family="Open Sans,sans-serif">1050</text><text x="58" y="82" text-anchor="middle" fill="#fff" font-size="11" font-family="Open Sans,sans-serif">Target</text></svg>Lorem ipsum</div>
  </div>
</section>

<section class="videos">
  <div class="video-frame" role="img" aria-label="Video still of a concert crowd under warm stage lights">
    <svg class="play" width="60" height="60" viewBox="0 0 60 60"><circle cx="30" cy="30" r="30" fill="var(--orange)"/><path d="M24 18v24l19-12z" fill="#fff"/></svg>
  </div>
  <div class="video-copy">
    <h2>EVENT VIDEOS</h2>
    <p>Catch the best moments from past Bandwick nights. Watch highlights from gigs, festivals and comedy shows, then share your favourite clips with friends and build a group for the next one. Every new member lowers the price, so the crowd you gather today makes tomorrow’s tickets cheaper for all of you.</p>
    <span class="btn">More Videos</span>
  </div>
</section>

<section class="contact" role="img" aria-label="Dark street map of the venue area behind the contact details">
  <div class="contact-info">
    <h3>CONTACT INFORMATIONS</h3>
    <div><svg width="12" height="16" viewBox="0 0 12 16"><path d="M6 0a6 6 0 0 0-6 6c0 4 6 10 6 10s6-6 6-10a6 6 0 0 0-6-6z" fill="#fff"/><circle cx="6" cy="6" r="2" fill="#333"/></svg>14 Larkfield Row</div>
    <div style="padding-left:22px">Lorem ipsum - NW1 8QP</div>
    <div style="padding-left:22px">Camden, London</div>
    <div><svg width="14" height="14" viewBox="0 0 14 14"><path d="M3 0l3 3-2 2c1 2 3 4 5 5l2-2 3 3-2 3C6 14 0 8 0 3z" fill="#fff"/></svg>020-7946-0318</div>
    <div><svg width="14" height="14" viewBox="0 0 14 14"><path d="M3 0l3 3-2 2c1 2 3 4 5 5l2-2 3 3-2 3C6 14 0 8 0 3z" fill="#fff"/></svg>020-7946-0392</div>
    <div><svg width="14" height="10" viewBox="0 0 14 10"><rect width="14" height="10" fill="#fff"/><path d="M0 0l7 6 7-6" fill="none" stroke="#333"/></svg>rlvo57@mailtrove.net</div>
  </div>
  <div class="reg">
    <h3>REGISTRATION FORM</h3>
    <div class="reg-grid">
      <div class="field">Name</div><div class="field">Surname</div>
      <div class="field">Phone Number</div><div class="field">Email Address</div>
      <div class="field select">Gender</div><div class="field select">Country</div>
    </div>
    <span class="submit">Submit</span>
  </div>
</section>

<footer class="site-footer">
  <div class="foot-col" style="left:100px">
    <h4>SUPPORT LINKS</h4>
    <ul class="links"><li>Home</li><li>About</li><li>Events</li><li>Blogs</li><li>Contact Us</li></ul>
  </div>
  <div class="foot-col news" style="left:430px">
    <h4>NEWSLETTER SIGN UP</h4>
    <p>Please sign up here for news</p>
    <div class="input">Email address</div>
    <span class="btn">SUBSCRIBE</span>
  </div>
  <div class="foot-col" style="left:840px">
    <h4>Social Media</h4>
    <div class="social"><span>Chatterbarn</span><span>Quillow</span><span>PingMesh</span><span>SMS</span><span>Email</span></div>
  </div>
  <div class="footer-bar">© 2016 Bandwick. All rights reserved. Terms of Use</div>
</footer>

</body>
</html>
```